Spirits Bottle Label for American Agave Spirit produced in Maryland

Need to revamp my spirits bottle label to a new innovative design. Looking for a minimalist design that would catch your eye on in a liquor store bottle. I open to designs. Looking for something a lot different than what I currently have wow me with your creativity.

Design Brief:

Logo Name: "Lumen" with the "H" positioned horizontally (emphasize the unique horizontal "H").
Color Scheme: Pink or Burgundy and gold (use these as primary colors). With gold being a accent color.
Motto: Include the phrase "Celebrate life with old and new friends" in a subtle, elegant font. Want to keep the 1947 but not as prominent as it is now.
Overall Feel: The design should convey warmth, celebration, and connection, blending a modern touch with timeless appeal.

I also attached a copy of my other brand bottle design thatI love. Reed & Flint is the name

Target Market(s)

21-65 Year old spirits drinkers, A label that is different than most spirits bottles. Want to catch the eyes of consumers

Industry/Entity Type

spirits industy

Colors

Designer to choose colors to be used in the design.

Requirements
Must have
• Motto, vibrant colors, minimist design
Should not have
• Need to look professional and not be so cluttered

```html
<!DOCTYPE html>
<html lang="en">
<head>
<meta charset="utf-8">
<title>Lumen 1962 Reposado Label</title>
<link rel="stylesheet" href="https://fonts.googleapis.com/css2?family=Bebas+Neue&family=Josefin+Sans:wght@400;600;700&family=Playfair+Display:wght@700;900&family=Montserrat:wght@500;700&display=swap">
<style>
  :root {
    --burgundy: #5c1413;
    --burgundy-deep: #4a0f0e;
    --blush: #e09a94;
    --cream: #fff6ec;
    --gold: #e6bf63;
    --gold-light: #fbe9a8;
    --gold-dark: #a8741f;
  }
  * { margin: 0; padding: 0; box-sizing: border-box; }
  html, body { width: 848px; height: 1200px; overflow: hidden; background: var(--burgundy); }
  .label {
    position: relative;
    width: 848px;
    height: 1200px;
    background: linear-gradient(90deg, var(--gold-dark), var(--gold-light) 12%, var(--gold) 50%, var(--gold-light) 88%, var(--gold-dark));
    padding: 17px 26px;
  }
  .panel {
    position: relative;
    width: 100%;
    height: 100%;
    background: var(--burgundy);
    overflow: hidden;
    color: var(--cream);
  }
  .crest { position: absolute; left: 0; top: 0; width: 796px; height: 500px; }
  .brand-name {
    position: absolute; left: 0; right: 0; top: 104px;
    text-align: center;
    font-family: "Bebas Neue", sans-serif;
    font-size: 168px; line-height: 1;
    letter-spacing: 4px;
    font-weight: 400;
    color: var(--burgundy);
  }
  .motto {
    position: absolute; left: 0; right: 0; top: 292px;
    text-align: center;
    font-family: "Josefin Sans", sans-serif;
    font-weight: 600;
    font-size: 28px; line-height: 38px;
    letter-spacing: 6px;
    color: var(--burgundy);
  }
  .vintage {
    position: absolute; left: 0; right: 0; top: 490px;
    text-align: center;
    font-family: "Playfair Display", serif;
    font-weight: 900;
    color: var(--cream);
    line-height: 1;
  }
  .vintage .year { display: block; font-size: 74px; }
  .vintage .style { display: block; font-size: 50px; letter-spacing: -1px; margin-top: 2px; }
  .agave-art {
    position: absolute; left: 281px; top: 650px; width: 234px; height: 166px;
    background: radial-gradient(ellipse at 50% 100%, var(--gold-light), var(--gold) 45%, rgba(230,191,99,0) 72%);
  }
  .dedication {
    position: absolute; left: 0; right: 0; top: 844px;
    text-align: center;
    font-family: "Montserrat", sans-serif;
    font-weight: 700;
    font-size: 19px; line-height: 29px;
    color: var(--cream);
  }
  .maker {
    position: absolute; left: 270px; top: 960px; width: 256px; height: 118px;
    text-align: center;
    font-family: "Playfair Display", serif;
    color: var(--gold);
    padding-top: 24px;
  }
  .maker .maker-name { display: block; font-size: 40px; font-weight: 700; letter-spacing: -1px; line-height: 1; }
  .maker .maker-sub { display: block; font-size: 19px; font-weight: 700; letter-spacing: 6px; margin-top: 8px; }
  .fine-print {
    position: absolute; left: 20px; right: 20px; top: 1102px;
    display: flex; justify-content: space-between; align-items: flex-end;
    color: var(--cream);
  }
  .volume { font-family: "Josefin Sans", sans-serif; font-size: 20px; line-height: 25px; }
  .established { font-family: "Montserrat", sans-serif; font-weight: 700; font-size: 19px; letter-spacing: -0.5px; margin-left: 60px; }
  .batch { font-family: "Montserrat", sans-serif; font-weight: 700; font-size: 17px; letter-spacing: 5px; }
</style>
</head>
<body>
<div class="label">
  <div class="panel">
    <svg class="crest" viewBox="0 0 796 500" aria-hidden="true">
      <path d="M32 0 H773 V110 A370.5 370.5 0 0 1 32 110 Z" fill="var(--blush)"/>
      <path id="arch" d="M170 110 Q402 10 634 110" fill="none"/>
      <text font-family="Josefin Sans, sans-serif" font-weight="700" font-size="23" letter-spacing="5" fill="var(--cream)" text-anchor="middle">
        <textPath href="#arch" startOffset="50%">AMERICAN AGAVE SPIRIT</textPath>
      </text>
      <path d="M184 340 L187 354 L200 357 L187 360 L184 374 L181 360 L168 357 L181 354 Z" fill="var(--gold)"/>
      <path d="M638 340 L641 354 L654 357 L641 360 L638 374 L635 360 L622 357 L635 354 Z" fill="var(--gold)"/>
    </svg>

    <h1 class="brand-name">LUMEN</h1>

    <p class="motto">CELEBRATE LIFE<br>WITH OLD AND NEW<br>FRIENDS</p>

    <div class="vintage">
      <span class="year">1962</span>
      <span class="style">REPOSADO</span>
    </div>

    <div class="agave-art" role="img" aria-label="Gold agave plant illustration"></div>

    <p class="dedication">IN HONOR OF MY GRANDPA,<br>WE NAMED THIS AMERICAN AGAVE 1962,<br>THE YEAR HE CAME HOME</p>

    <div class="maker">
      <span class="maker-name">R.T.VALE</span>
      <span class="maker-sub">DISTILLERS</span>
    </div>

    <div class="fine-print">
      <p class="volume">750 ml<br>Alc. 40% by Vol.</p>
      <p class="established">EST.2016</p>
      <p class="batch">SMALL BATCH</p>
    </div>
  </div>
</div>
</body>
</html>
```